Brindlemoor Client Journey To Success

I need a one-page document that graphically shows the client's journey working with Brindlemoor from initial assessment to completed project. I want the journey to start at the "basecamp logo" and reach 4 summits (little mountain logos...) .

I'd like the imagery to convey the client starting at basecamp, and moving to each summit. Each summit, should list the subtext under each, as listed on the pdf doc i provided.

The description for the basecamp and 4 summits is attached.

I need the brochure to look like the other brochure that you did for me (attached) .

Target Market(s)

Restaurant Owners

Industry/Entity Type

Construction Management

Font styles to use
Sans Serif

Colors
EB3D1F
EC4F4E
F09395
F8D3D4
FCEDEE

Requirements
Must have
• My logo. Title: Client Journey To Success. Subtitle: The 4 Summits

```html
<!DOCTYPE html>
<html lang="en">
<head>
<meta charset="utf-8">
<title>Brindlemoor Development – Our Client's Journey</title>
<link rel="stylesheet" href="https://fonts.googleapis.com/css2?family=Montserrat:wght@500;600;700;800&family=Arimo:wght@400;700&display=swap">
<style>
:root{
  --red:#c8161d;
  --red-deep:#a50f14;
  --red-bright:#eb3d1f;
  --ink:#111111;
  --navy:#111827;
  --paper:#ffffff;
  --charcoal:#2b2b2b;
  --charcoal-light:#4a4a4a;
  --blush:#f8d3d4;
  --mist:#fcedee;
  --lilac:#d9c3cf;
}
*{margin:0;padding:0;box-sizing:border-box}
html,body{width:800px;height:1200px;overflow:hidden;background:var(--paper)}
.flyer{position:relative;width:800px;height:1200px;background:var(--paper);font-family:"Arimo",Arial,sans-serif;color:var(--ink);overflow:hidden}

.header-art{position:absolute;left:0;top:0}
.journey-title{position:absolute;left:457px;top:50px;padding-left:20px;border-left:4px solid var(--paper);color:var(--paper);font-family:"Montserrat",sans-serif;font-weight:800;line-height:1}
.journey-title .kicker{display:block;font-size:25px;letter-spacing:.5px}
.journey-title .main{display:block;font-size:40px;margin-top:4px}

.brand{position:absolute;left:36px;top:44px;width:200px}
.brand-square{width:84px;height:84px;margin-left:38px;background:var(--red)}
.brand-name{margin-top:62px;font-family:"Montserrat",sans-serif;font-weight:800;font-size:12.5px;color:var(--ink);letter-spacing:.2px}

.headline{position:absolute;left:34px;top:238px;font-family:"Montserrat",sans-serif;font-size:43px;line-height:65px;letter-spacing:-.6px;color:var(--ink);font-weight:500}
.headline .accent{color:var(--red);font-weight:800;letter-spacing:-.2px}

.intro{position:absolute;left:34px;top:468px;width:350px;padding-left:17px;border-left:4px solid var(--red);font-size:12px;line-height:15.5px;color:#222}

.photo{position:absolute;left:0;top:574px;width:428px;height:490px;background:linear-gradient(180deg,#f4ecf0 0%,var(--lilac) 55%,#c9aab9 100%)}
.photo-fade{position:absolute;left:428px;top:850px;width:372px;height:214px;background:linear-gradient(180deg,rgba(252,237,238,0) 0%,var(--mist) 45%,#e6cfd8 100%)}

.timeline-line{position:absolute;left:477px;top:200px;width:3px;height:770px;background:var(--red-deep)}
.marker{position:absolute;left:454px;width:50px;height:54px}

.stage{position:absolute;left:528px;font-family:"Montserrat",sans-serif}
.stage h2{font-weight:800;font-size:19.5px;line-height:22px;color:var(--ink)}
.stage h2 .step{display:block;color:var(--red)}
.stage.basecamp h2{color:var(--red)}
.tasks{list-style:none;margin-top:12px;margin-left:4px}
.tasks li{display:flex;align-items:center;height:25px;font-family:"Arimo",sans-serif;font-weight:700;font-size:12px;color:#1a1a1a}
.tasks svg{flex:none;margin-right:12px}

.footer-art{position:absolute;left:0;top:1058px}
.call{position:absolute;left:35px;top:1098px;font-family:"Montserrat",sans-serif;font-weight:800;font-size:16px;color:var(--red-bright);letter-spacing:.3px}
.contact-row{position:absolute;top:1134px;display:flex;align-items:center;color:var(--paper)}
.contact-row .icon{flex:none;width:24px;height:24px;border-radius:3px;background:var(--red);display:flex;align-items:center;justify-content:center;margin-right:12px}
.phone{left:35px;font-family:"Montserrat",sans-serif;font-weight:800;font-size:25px}
.email{left:280px;font-size:13px}
.visit{position:absolute;left:553px;top:1098px;font-family:"Montserrat",sans-serif;font-weight:800;font-size:16px;color:var(--paper)}
.web{left:553px;font-size:14px;font-weight:700}
.web .icon{background:var(--paper)}
</style>
</head>
<body>
<main class="flyer">

  <svg class="header-art" width="800" height="190" viewBox="0 0 800 190" aria-hidden="true">
    <defs>
      <linearGradient id="bandGrad" x1="0" y1="0" x2="1" y2="0">
        <stop offset="0" stop-color="#8e0c10"/>
        <stop offset=".5" stop-color="#c8161d"/>
        <stop offset="1" stop-color="#b31218"/>
      </linearGradient>
    </defs>
    <polygon points="293,0 800,0 800,150 440,150" fill="url(#bandGrad)"/>
    <polygon points="217,0 266,0 344,126 295,126" fill="var(--red)"/>
    <polygon points="300,132 342,132 384,184 342,184" fill="var(--navy)"/>
  </svg>

  <h1 class="journey-title"><span class="kicker">OUR CLIENT’S</span><span class="main">JOURNEY</span></h1>

  <div class="brand">
    <div class="brand-square"></div>
    <p class="brand-name">BRINDLEMOOR DEVELOPMENT</p>
  </div>

  <p class="headline">A RUTHLESS<br><span class="accent">COMMITMENT</span><br>TO BIG RESULTS</p>

  <p class="intro">Brindlemoor Development Services LLC is a group of Dynamic Professionals with deep histories of managing significant projects inside of the Restaurant, Retail and Entertainment space. An intimate knowledge and proven track record of managing Design, Procurement, Architectural, and Construction efforts simultaneously to produce Undeniable Results.</p>

  <div class="photo" role="img" aria-label="Smiling construction worker in a yellow hard hat, plaid shirt and blue overalls, arms crossed, in front of a hazy city skyline"></div>
  <div class="photo-fade" aria-hidden="true"></div>

  <div class="timeline-line" aria-hidden="true"></div>

  <!-- markers -->
  <svg class="marker" style="top:169px" viewBox="0 0 50 54" aria-hidden="true">
    <polygon points="25,1 48,14 48,40 25,53 2,40 2,14" fill="var(--red)"/>
    <polygon points="25,19 37,37 13,37" fill="#fff"/>
    <rect x="24" y="10" width="1.6" height="10" fill="#fff"/>
    <polygon points="25.6,10 32,12.5 25.6,15" fill="#fff"/>
    <polygon points="25,28 28.5,37 21.5,37" fill="var(--red)"/>
  </svg>
  <svg class="marker" style="top:329px" viewBox="0 0 50 54" aria-hidden="true">
    <polygon points="25,1 48,14 48,40 25,53 2,40 2,14" fill="var(--red)"/>
    <polygon points="25,19 38,38 12,38" fill="#fff"/>
    <rect x="24" y="11" width="1.6" height="9" fill="#fff"/>
    <polygon points="25.6,11 31,13 25.6,15" fill="#fff"/>
  </svg>
  <svg class="marker" style="top:569px" viewBox="0 0 50 54" aria-hidden="true">
    <polygon points="25,1 48,14 48,40 25,53 2,40 2,14" fill="var(--red)"/>
    <polygon points="27,20 39,38 13,38" fill="#fff"/>
    <circle cx="19" cy="16" r="2.5" fill="#fff"/>
    <rect x="17.5" y="19" width="3" height="9" fill="#fff"/>
  </svg>
  <svg class="marker" style="top:738px" viewBox="0 0 50 54" aria-hidden="true">
    <polygon points="25,1 48,14 48,40 25,53 2,40 2,14" fill="var(--red)"/>
    <polygon points="30,17 40,38 16,38" fill="#fff"/>
    <polygon points="17,27 24,38 10,38" fill="#fff"/>
    <rect x="29.2" y="11" width="1.6" height="7" fill="#fff"/>
    <polygon points="30.8,11 35,12.5 30.8,14" fill="#fff"/>
  </svg>
  <svg class="marker" style="top:932px" viewBox="0 0 50 54" aria-hidden="true">
    <polygon points="25,1 48,14 48,40 25,53 2,40 2,14" fill="var(--red)"/>
    <circle cx="25" cy="19" r="3" fill="#fff"/>
    <polygon points="17,22 33,22 28,28 28,38 22,38 22,28" fill="#fff"/>
    <rect x="31" y="10" width="1.6" height="13" fill="#fff"/>
    <polygon points="32.6,10 37,12 32.6,14" fill="#fff"/>
  </svg>

  <section class="stage basecamp" style="top:183px">
    <h2>BASECAMP</h2>
    <ul class="tasks">
      <li><svg width="11" height="11" viewBox="0 0 11 11"><rect x=".7" y="1.7" width="8.6" height="8.6" fill="none" stroke="var(--red)" stroke-width="1.2"/><path d="M2.5 5.5l2 2L10 1" fill="none" stroke="var(--red)" stroke-width="1.4"/></svg>Client Assessment</li>
      <li><svg width="11" height="11" viewBox="0 0 11 11"><rect x=".7" y="1.7" width="8.6" height="8.6" fill="none" stroke="var(--red)" stroke-width="1.2"/><path d="M2.5 5.5l2 2L10 1" fill="none" stroke="var(--red)" stroke-width="1.4"/></svg>Determine Project Goals</li>
      <li><svg width="11" height="11" viewBox="0 0 11 11"><rect x=".7" y="1.7" width="8.6" height="8.6" fill="none" stroke="var(--red)" stroke-width="1.2"/><path d="M2.5 5.5l2 2L10 1" fill="none" stroke="var(--red)" stroke-width="1.4"/></svg>Proposal &amp; Fees</li>
    </ul>
  </section>

  <section class="stage" style="top:335px">
    <h2><span class="step">SUMMIT 1</span>PRECONSTRUCTION</h2>
    <ul class="tasks">
      <li><svg width="11" height="11" viewBox="0 0 11 11"><rect x=".7" y="1.7" width="8.6" height="8.6" fill="none" stroke="var(--red)" stroke-width="1.2"/><path d="M2.5 5.5l2 2L10 1" fill="none" stroke="var(--red)" stroke-width="1.4"/></svg>Develop Project Plan</li>
      <li><svg width="11" height="11" viewBox="0 0 11 11"><rect x=".7" y="1.7" width="8.6" height="8.6" fill="none" stroke="var(--red)" stroke-width="1.2"/><path d="M2.5 5.5l2 2L10 1" fill="none" stroke="var(--red)" stroke-width="1.4"/></svg>Develop Risk Assessment &amp; Plan</li>
      <li><svg width="11" height="11" viewBox="0 0 11 11"><rect x=".7" y="1.7" width="8.6" height="8.6" fill="none" stroke="var(--red)" stroke-width="1.2"/><path d="M2.5 5.5l2 2L10 1" fill="none" stroke="var(--red)" stroke-width="1.4"/></svg>Devlelop Schedule</li>
      <li><svg width="11" height="11" viewBox="0 0 11 11"><rect x=".7" y="1.7" width="8.6" height="8.6" fill="none" stroke="var(--red)" stroke-width="1.2"/><path d="M2.5 5.5l2 2L10 1" fill="none" stroke="var(--red)" stroke-width="1.4"/></svg>Develop Budget</li>
      <li><svg width="11" height="11" viewBox="0 0 11 11"><rect x=".7" y="1.7" width="8.6" height="8.6" fill="none" stroke="var(--red)" stroke-width="1.2"/><path d="M2.5 5.5l2 2L10 1" fill="none" stroke="var(--red)" stroke-width="1.4"/></svg>Develop Team</li>
      <li><svg width="11" height="11" viewBox="0 0 11 11"><rect x=".7" y="1.7" width="8.6" height="8.6" fill="none" stroke="var(--red)" stroke-width="1.2"/><path d="M2.5 5.5l2 2L10 1" fill="none" stroke="var(--red)" stroke-width="1.4"/></svg>GC,Sub, Consultants Contracts</li>
    </ul>
  </section>

  <section class="stage" style="top:573px">
    <h2><span class="step">SUMMIT 2</span>EXECUTION</h2>
    <ul class="tasks">
      <li><svg width="11" height="11" viewBox="0 0 11 11"><rect x=".7" y="1.7" width="8.6" height="8.6" fill="none" stroke="var(--red)" stroke-width="1.2"/><path d="M2.5 5.5l2 2L10 1" fill="none" stroke="var(--red)" stroke-width="1.4"/></svg>Acquire Permits</li>
      <li><svg width="11" height="11" viewBox="0 0 11 11"><rect x=".7" y="1.7" width="8.6" height="8.6" fill="none" stroke="var(--red)" stroke-width="1.2"/><path d="M2.5 5.5l2 2L10 1" fill="none" stroke="var(--red)" stroke-width="1.4"/></svg>PreConstruction Meeting</li>
      <li><svg width="11" height="11" viewBox="0 0 11 11"><rect x=".7" y="1.7" width="8.6" height="8.6" fill="none" stroke="var(--red)" stroke-width="1.2"/><path d="M2.5 5.5l2 2L10 1" fill="none" stroke="var(--red)" stroke-width="1.4"/></svg>Project Start</li>
    </ul>
  </section>

  <section class="stage" style="top:747px">
    <h2><span class="step">SUMMIT 3</span>PROJECT MANAGEMENT</h2>
    <ul class="tasks">
      <li><svg width="11" height="11" viewBox="0 0 11 11"><rect x=".7" y="1.7" width="8.6" height="8.6" fill="none" stroke="var(--red)" stroke-width="1.2"/><path d="M2.5 5.5l2 2L10 1" fill="none" stroke="var(--red)" stroke-width="1.4"/></svg>Shared Consciousness Meetings</li>
      <li><svg width="11" height="11" viewBox="0 0 11 11"><rect x=".7" y="1.7" width="8.6" height="8.6" fill="none" stroke="var(--red)" stroke-width="1.2"/><path d="M2.5 5.5l2 2L10 1" fill="none" stroke="var(--red)" stroke-width="1.4"/></svg>Pressurized Collaboration</li>
      <li><svg width="11" height="11" viewBox="0 0 11 11"><rect x=".7" y="1.7" width="8.6" height="8.6" fill="none" stroke="var(--red)" stroke-width="1.2"/><path d="M2.5 5.5l2 2L10 1" fill="none" stroke="var(--red)" stroke-width="1.4"/></svg>Schedule Management</li>
      <li><svg width="11" height="11" viewBox="0 0 11 11"><rect x=".7" y="1.7" width="8.6" height="8.6" fill="none" stroke="var(--red)" stroke-width="1.2"/><path d="M2.5 5.5l2 2L10 1" fill="none" stroke="var(--red)" stroke-width="1.4"/></svg>Run O.O.D.A. Loop</li>
    </ul>
  </section>

  <section class="stage" style="top:937px">
    <h2><span class="step">SUMMIT 4</span>COMPLETION</h2>
    <ul class="tasks">
      <li><svg width="11" height="11" viewBox="0 0 11 11"><rect x=".7" y="1.7" width="8.6" height="8.6" fill="none" stroke="var(--red)" stroke-width="1.2"/><path d="M2.5 5.5l2 2L10 1" fill="none" stroke="var(--red)" stroke-width="1.4"/></svg>Closeout</li>
    </ul>
  </section>

  <svg class="footer-art" width="800" height="142" viewBox="0 0 800 142" aria-hidden="true">
    <defs>
      <linearGradient id="darkGrad" x1="0" y1="0" x2="1" y2="0">
        <stop offset="0" stop-color="#2a2a2a"/>
        <stop offset=".6" stop-color="#505050"/>
        <stop offset="1" stop-color="#3a3a3a"/>
      </linearGradient>
      <linearGradient id="footRed" x1="0" y1="0" x2="1" y2="0">
        <stop offset="0" stop-color="#a50f14"/>
        <stop offset="1" stop-color="#c8161d"/>
      </linearGradient>
    </defs>
    <rect x="0" y="0" width="800" height="142" fill="url(#footRed)"/>
    <polygon points="0,16 490,16 550,142 0,142" fill="url(#darkGrad)"/>
  </svg>

  <p class="call">CALL US NOW!</p>
  <p class="contact-row phone"><span class="icon"><svg width="14" height="14" viewBox="0 0 24 24"><path d="M6.6 10.8a15 15 0 0 0 6.6 6.6l2.2-2.2c.3-.3.7-.4 1-.2 1.1.4 2.3.6 3.6.6.6 0 1 .4 1 1V20c0 .6-.4 1-1 1A17 17 0 0 1 3 4c0-.6.4-1 1-1h3.5c.6 0 1 .4 1 1 0 1.3.2 2.5.6 3.6.1.3 0 .7-.2 1l-2.3 2.2z" fill="#fff"/></svg></span>214-555-0187</p>
  <p class="contact-row email"><span class="icon"><svg width="14" height="12" viewBox="0 0 14 12"><rect x=".8" y="1" width="12.4" height="10" fill="none" stroke="#fff" stroke-width="1.4"/><path d="M1 1.5l6 5 6-5" fill="none" stroke="#fff" stroke-width="1.4"/></svg></span>hello@brindlemoordev.com</p>
  <p class="visit">VISIT US</p>
  <p class="contact-row web"><span class="icon"><svg width="16" height="16" viewBox="0 0 16 16"><circle cx="8" cy="8" r="6.5" fill="none" stroke="var(--red)" stroke-width="1.3"/><ellipse cx="8" cy="8" rx="2.8" ry="6.5" fill="none" stroke="var(--red)" stroke-width="1.1"/><path d="M1.5 8h13M2.5 4.8h11M2.5 11.2h11" stroke="var(--red)" stroke-width="1"/></svg></span>www.brindlemoordev.com</p>

</main>
</body>
</html>
```